Ferrant Valley Zoning Council Business Cards

We're looking for a business card design, simple as that. We're a local government agency that mainly performs building code enforcement, transportation planning, floodplain management, and GIS for Tobelle Parish in Louisiana, and other surround parishes. So you're not having to Google anything, GIS is, at it's core, mapping. Building Code Enforcement is just that, nothing more. Floodplain Management is to make sure the public is within what the government

Contact Information for Business Card

Our Address is

517 Marwick Street
Halvern Ridge, KS 66921

Our phone is 6205529137
Our fax is 6205529142
Our website is www.fvzc.info
My email is dana@fvzc.info

Font styles to use
Serif
Sans Serif

Colors

Designer to choose colors to be used in the design.

Requirements
Must have
• I'm attaching our logo(several versions) that must be incorporated. The design should fit well with our existing logo. I can send photoshop files for our logo if needed. If possible, I'd like to be able to add names/info to each card for all of our employees once this is done.
Nice to have
• The Louisiana state seal is a bonus, and isn't specifically required.

```html
<!DOCTYPE html>
<html lang="en">
<head>
<meta charset="utf-8">
<title>Ferrant Valley Zoning Council – Business Cards</title>
<link rel="stylesheet" href="https://fonts.googleapis.com/css2?family=Lato:wght@400;700&family=Montserrat:wght@300;700&display=swap">
<style>
  :root {
    --backdrop: #2a2a2c;
    --card: #0b0b0d;
    --ink: #f4f4f4;
    --muted: #6e6e72;
    --rule: #4a4636;
    --icon-fill: #e9e9e9;
  }
  html, body {
    margin: 0;
    width: 1200px;
    height: 1163px;
    overflow: hidden;
    background: var(--backdrop);
  }
  .canvas {
    position: relative;
    width: 1200px;
    height: 1163px;
  }
  .card {
    position: absolute;
    left: 220px;
    width: 760px;
    height: 434px;
    background: var(--card);
    box-shadow: 0 18px 40px rgba(0,0,0,.55);
  }
  .card--front { top: 110px; }
  .card--back  { top: 618px; }

  .contact {
    position: absolute;
    left: 140px;
    top: 56px;
    width: 280px;
    text-align: center;
    font-family: "Lato", sans-serif;
  }
  .contact__name {
    margin: 0;
    font-size: 33px;
    font-weight: 700;
    color: var(--ink);
    letter-spacing: .3px;
  }
  .contact__role {
    margin: 2px 0 0;
    font-size: 17px;
    color: var(--muted);
  }
  .contact__rule {
    height: 1px;
    background: var(--rule);
    margin: 12px auto;
    width: 200px;
  }
  .contact__icons {
    display: flex;
    justify-content: center;
    gap: 6px;
    margin: -4px 0 -2px;
  }
  .contact__lines {
    margin: 0;
    font-size: 19px;
    line-height: 26px;
    color: var(--muted);
    letter-spacing: .5px;
  }
  .contact__org {
    margin: 0;
    font-size: 17px;
    font-weight: 400;
    color: var(--ink);
    white-space: nowrap;
  }
  .contact__address {
    margin: 2px 0 0;
    font-size: 18px;
    line-height: 23px;
    color: var(--muted);
    white-space: nowrap;
  }

  .brand {
    position: absolute;
    right: 60px;
    top: 150px;
    width: 250px;
    display: flex;
    align-items: center;
    gap: 14px;
    font-family: "Lato", sans-serif;
    font-weight: 700;
    font-size: 22px;
    line-height: 28px;
    color: var(--ink);
  }
  .brand__mark {
    flex: none;
    width: 22px;
    height: 22px;
    background: var(--ink);
  }

  .wordmark {
    position: absolute;
    left: 170px;
    top: 130px;
    font-family: "Montserrat", sans-serif;
  }
  .wordmark__short {
    margin: 0;
    font-size: 150px;
    font-weight: 700;
    line-height: 1;
    color: var(--ink);
    letter-spacing: 2px;
  }
  .wordmark__full {
    margin: 6px 0 0 4px;
    font-size: 27px;
    font-weight: 300;
    color: var(--muted);
    letter-spacing: 1.5px;
  }
</style>
</head>
<body>
<main class="canvas">

  <section class="card card--front">
    <div class="contact">
      <h1 class="contact__name">Marcus Hale</h1>
      <p class="contact__role">Representative</p>
      <div class="contact__rule"></div>
      <div class="contact__icons">
        <svg width="24" height="24" viewBox="0 0 24 24" aria-label="Phone">
          <circle cx="12" cy="12" r="11" fill="var(--icon-fill)"/>
          <path d="M8 6.5c-.8.6-1.4 1.6-1 3 .8 2.7 3.8 6 6.6 7.3 1.3.6 2.4.1 3-.7l.3-.6-2.4-1.8-1.2 1c-1.3-.6-3-2.4-3.6-3.7l1-1.2-1.7-2.5z" fill="var(--card)"/>
        </svg>
        <svg width="24" height="24" viewBox="0 0 24 24" aria-label="Fax">
          <circle cx="12" cy="12" r="11" fill="var(--icon-fill)"/>
          <rect x="8.5" y="5.5" width="7" height="4" fill="var(--card)"/>
          <rect x="6" y="10" width="12" height="6" rx="1" fill="var(--card)"/>
          <rect x="8.5" y="14" width="7" height="4.5" fill="var(--card)"/>
        </svg>
        <svg width="24" height="24" viewBox="0 0 24 24" aria-label="Email">
          <circle cx="12" cy="12" r="11" fill="var(--icon-fill)"/>
          <rect x="6" y="8" width="12" height="8" fill="none" stroke="var(--card)" stroke-width="1.6"/>
          <path d="M6 8l6 4.5L18 8" fill="none" stroke="var(--card)" stroke-width="1.6"/>
        </svg>
      </div>
      <div class="contact__rule"></div>
      <p class="contact__lines">6205529137<br>6205529142<br>dana@fvzc.info</p>
      <div class="contact__rule"></div>
      <p class="contact__org">Ferrant Valley Zoning Council</p>
      <p class="contact__address">517 Marwick Street<br>Halvern Ridge, KS 66921</p>
    </div>

    <div class="brand">
      <span class="brand__mark"></span>
      <span>Ferrant Valley Zoning Council</span>
    </div>
  </section>

  <section class="card card--back">
    <div class="wordmark">
      <p class="wordmark__short">FVZC</p>
      <p class="wordmark__full">Ferrant Valley Zoning Council</p>
    </div>
  </section>

</main>
</body>
</html>
```